Art Exhibit Invitation Design

This is an exhibit invitation for a three-artist show. The final postcard will be 6X9 and placed in an envelope of 6 1/2 by 9 1/2. I have placed two logos we use (although the logo color is pink, it is possible that the color can be changed. The artists are Marla Quenby, Leona Whitcombe, and Rosalind Verhoff. The corresponding images are Leona (apple tree), Rosalind (green celadon), and Marla (Poppies). The show runs July 8 - Aug 25. The opening Reception is Saturday, July 8 from 3-5pm. I would like this done in Adobe InDesign. Since the postcard is being put in an envelope, information about the exhibit can be put on the back (no return address or stamp will be needed) .
The Pemberly Gallery is located at 2417 E Fenwick Ridge Rd, Yakima WA 98907. our phone is (509) 555-0193.
The exhibit title is Quiet Weather.
Leona works in Pastel, Marla is a painter, and Rosalnd is a ceramicist.

```html
<!DOCTYPE html>
<html lang="en">
<head>
<meta charset="utf-8">
<title>Pemberly – Quiet Weather Invitation</title>
<link rel="stylesheet" href="https://fonts.googleapis.com/css2?family=Josefin+Sans:wght@300;400;700&family=Poppins:wght@700;800&display=swap">
<style>
:root{
  --stage:#a3a3a3;
  --magenta:#e8168c;
  --magenta-deep:#d40f7e;
  --pink-soft:#f9d3e7;
  --peach:#f7b99c;
  --ink:#1d1a1c;
  --white:#ffffff;
  --tape:rgba(236,120,170,.75);
}
*{box-sizing:border-box;margin:0;padding:0}
html,body{width:1200px;height:2495px;overflow:hidden;background:var(--stage)}
body{position:relative;font-family:"Josefin Sans",sans-serif}

.brand-mark{position:absolute;left:41px;top:46px;font-family:"Josefin Sans",sans-serif;font-weight:700;font-size:70px;letter-spacing:6px;color:var(--white);line-height:1}

.card{position:absolute;left:60px;width:1106px;transform:scale(.9686);transform-origin:0 0;overflow:hidden;
  background:linear-gradient(180deg,var(--pink-soft) 0%,#f6b6cf 35%,var(--peach) 55%,#ee5fa7 78%,var(--magenta) 100%);
  box-shadow:0 4px 8px rgba(0,0,0,.35)}
.card--artists{top:990px;height:738px}
.card--details{top:1739px;height:735px}

.header{position:absolute;left:0;top:0;width:1106px;height:152px}
.header svg{position:absolute;inset:0}
.wordmark{position:absolute;top:50px;left:44px;font-weight:700;font-size:66px;letter-spacing:6px;line-height:1;white-space:nowrap}
.wordmark--dark{color:var(--ink)}
.wordmark--light{color:var(--white)}
.title{position:absolute;top:50px;right:40px;font-weight:700;font-size:62px;line-height:1;letter-spacing:1px;white-space:nowrap}
.title--light{color:var(--white)}
.title--dark{color:var(--ink)}
.title .accent{color:var(--magenta)}

.artwork{position:absolute;background:var(--white);padding:12px 15px}
.artwork .fill{width:100%;height:100%}
.tape{position:absolute;width:110px;height:36px;background:var(--tape);transform:rotate(-45deg)}

.artist{position:absolute;width:335px;text-align:center}
.artist .name{display:inline-block;background:var(--white);color:var(--ink);font-weight:400;font-size:29px;padding:6px 36px 2px;border-radius:3px 14px 3px 14px;white-space:nowrap}
.artist .role{margin-top:18px;color:var(--white);font-weight:400;font-size:24px;white-space:nowrap}

.footer-bar{position:absolute;left:0;right:0;bottom:0;height:63px;background:var(--ink);color:var(--white);font-size:23px;padding:22px 0 0 40px;white-space:nowrap}
.footer-bar strong{font-weight:700}
.footer-bar span{font-weight:300}

.show-dates{position:absolute;left:663px;top:195px;width:408px;text-align:center;font-family:"Poppins",sans-serif;font-weight:800;font-size:44px;line-height:1.1;white-space:nowrap}
.show-dates .label{color:var(--ink)}
.show-dates .range{color:var(--magenta)}
.reception{position:absolute;left:656px;top:317px;width:414px;height:273px;border:2px dashed rgba(255,255,255,.85);border-radius:14px;text-align:center;font-family:"Poppins",sans-serif;padding-top:22px}
.reception .lead{color:var(--ink);font-weight:700;font-size:31px;line-height:1.3}
.reception .when{color:var(--white);font-weight:800;font-size:42px;line-height:1.15;margin-top:10px}

.location{position:absolute;left:32px;top:648px;color:var(--white);white-space:nowrap}
.location strong{display:block;font-weight:700;font-size:25px}
.location span{display:block;font-weight:300;font-size:25px;margin-top:10px}
.divider{position:absolute;left:560px;top:646px;width:2px;height:66px;background:var(--white)}
.phone{position:absolute;left:584px;top:650px;display:flex;align-items:center;gap:10px;color:var(--white);font-weight:700;font-size:50px;white-space:nowrap}
</style>
</head>
<body>

<div class="brand-mark">PEMBERLY</div>

<section class="card card--artists">
  <div class="header">
    <svg width="1106" height="152" viewBox="0 0 1106 152">
      <path d="M478 0 C520 0 515 40 535 95 C552 140 568 150 600 150 L1106 150 L1106 0 Z" fill="var(--magenta)"/>
      <path d="M478 0 C520 0 515 40 535 95 C552 140 568 150 600 150" fill="none" stroke="var(--ink)" stroke-width="5"/>
    </svg>
    <div class="wordmark wordmark--dark">PEMBERLY</div>
    <div class="title title--light">QUIET WEATHER</div>
  </div>

  <div class="artwork" style="left:36px;top:213px;width:335px;height:320px">
    <div class="fill" role="img" aria-label="Marla Quenby painting of orange poppies in a white vase" style="background:linear-gradient(160deg,#c9502a 0%,#e9e3a0 40%,#d2552f 60%,#2f8c8a 100%)"></div>
  </div>
  <div class="tape" style="left:20px;top:230px"></div>

  <div class="artwork" style="left:388px;top:213px;width:333px;height:320px">
    <div class="fill" role="img" aria-label="Leona Whitcombe pastel of an apple tree" style="background:linear-gradient(180deg,#d9b5a6 0%,#6f8a4e 45%,#4d7a3d 70%,#7aa05a 100%)"></div>
  </div>

  <div class="artwork" style="left:736px;top:213px;width:334px;height:320px">
    <div class="fill" role="img" aria-label="Rosalind Verhoff celadon ceramic plate" style="background:radial-gradient(circle at 50% 48%,#bfe2d8 0%,#cfe3c6 45%,#9fd4cf 60%,#14162a 72%,#0c0e1f 100%)"></div>
  </div>
  <div class="tape" style="left:718px;top:230px"></div>

  <div class="artist" style="left:42px;top:555px"><div class="name">Marla Quenby</div><div class="role">Marla is a painter</div></div>
  <div class="artist" style="left:388px;top:555px"><div class="name">Leona Whitcombe</div><div class="role">Leona works in Pastels</div></div>
  <div class="artist" style="left:736px;top:555px"><div class="name">Rosalind Verhoff</div><div class="role">Rosalind is a ceramicist</div></div>

  <div class="footer-bar"><strong>THE PEMBERLY GALLERY IS LOCATED AT</strong> <span>2417 E Fenwick Ridge Rd, Yakima WA 98907.</span></div>
</section>

<section class="card card--details">
  <div class="header">
    <svg width="1106" height="152" viewBox="0 0 1106 152">
      <path d="M0 0 L522 0 C496 15 488 60 470 100 C455 135 440 150 410 150 L0 150 Z" fill="var(--magenta)"/>
      <path d="M522 0 C496 15 488 60 470 100 C455 135 440 150 410 150" fill="none" stroke="var(--ink)" stroke-width="5"/>
    </svg>
    <div class="wordmark wordmark--light">PEMBERLY</div>
    <div class="title title--dark">QUIET <span class="accent">WEATHER</span></div>
  </div>

  <div class="artwork" style="left:36px;top:190px;width:595px;height:410px;padding:18px 22px">
    <div class="fill" role="img" aria-label="Exterior of The Pemberly Gallery building at dusk" style="background:linear-gradient(180deg,#2a3f8a 0%,#3e5396 30%,#7a4b3a 55%,#5b4a45 75%,#3a3a3e 100%)"></div>
  </div>
  <div class="tape" style="left:20px;top:205px"></div>
  <div class="tape" style="left:545px;top:575px"></div>

  <div class="show-dates"><div class="label">THE SHOW RUNS</div><div class="range">JULY 8 - AUG 25</div></div>
  <div class="reception">
    <div class="lead">THE OPENING<br>RECEPTION IS</div>
    <div class="when">SATURDAY,<br>JULY 8 FROM<br>3-5 PM</div>
  </div>

  <div class="location"><strong>THE PEMBERLY GALLERY IS LOCATED AT</strong><span>2417 E Fenwick Ridge Rd, Yakima WA 98907.</span></div>
  <div class="divider"></div>
  <div class="phone">
    <svg width="52" height="52" viewBox="0 0 56 56" aria-hidden="true">
      <circle cx="28" cy="28" r="27" fill="var(--white)"/>
      <path d="M19 14 L24 14 L26 22 L22 25 C24 30 27 33 32 35 L35 31 L43 33 L43 38 C43 41 40 43 37 42 C26 40 17 31 15 20 C14 17 16 14 19 14 Z" fill="var(--magenta)"/>
    </svg>
    (509) 555-0193
  </div>
</section>

</body>
</html>
```